Modern Business Card For A Digital Advertising Company

I'll be print on the Tarn Prints Velour paper http://us.tarnprints.example/products/velour/business-cards.html
Need's to be modern and use the color palette of the logo or gray scales. I think integrating the pixelation of the logo in to the card and having it wrap from one side to the other could be interesting. My company provides ad operations, web development, and number of other services to websites around the world. You can see my website at http://www.pixelharbor.example
Contact info on the card needs to have
Dana Welloby
President
p.555.318.4406
dana@pixelharbor.example
http://www.pixelharbor.example
Doesn't necessarily need to be in that order
Target Market(s)
Website owners
Industry/Entity Type
Business
Look and feel

```html
<!DOCTYPE html>
<html lang="en">
<head>
<meta charset="utf-8">
<title>Pixel Harbor – Business Card</title>
<link href="https://fonts.googleapis.com/css2?family=Arvo:wght@400;700&display=swap" rel="stylesheet">
<style>
  :root {
    --green: #8dc63f;
    --ink: #4a4a4a;
    --card: #ffffff;
    --backdrop: #3b3b3b;
  }
  * { margin: 0; padding: 0; box-sizing: border-box; }
  html, body { width: 1200px; height: 900px; overflow: hidden; }
  body {
    background: var(--backdrop);
    font-family: "Arvo", Georgia, serif;
    position: relative;
  }
  .card {
    position: absolute;
    top: 307px;
    width: 515px;
    height: 286px;
    background: var(--card);
  }
  .card--front { left: 72px; }
  .card--back { left: 613px; }

  .brand {
    position: absolute;
    display: flex;
    align-items: center;
    gap: 10px;
    color: var(--green);
    font-weight: 700;
  }
  .brand__square { background: var(--green); flex: none; }
  .card--front .brand { left: 44px; top: 120px; font-size: 28px; }
  .card--front .brand__square { width: 26px; height: 26px; }
  .card--back .brand { left: 44px; top: 128px; font-size: 19px; }
  .card--back .brand__square { width: 18px; height: 18px; }

  .services {
    position: absolute;
    right: 0;
    top: 68px;
    list-style: none;
    display: flex;
    flex-direction: column;
    align-items: flex-end;
    gap: 4px;
  }
  .services__item {
    background: var(--green);
    color: #fff;
    font-size: 15.5px;
    line-height: 22px;
    height: 22px;
    padding: 0 28px 0 12px;
    white-space: nowrap;
  }

  .contact {
    position: absolute;
    left: 264px;
    top: 78px;
    border-left: 1.5px solid var(--green);
    padding: 6px 0 10px 17px;
    height: 134px;
  }
  .contact__name { color: var(--green); font-size: 22px; font-weight: 400; line-height: 1.1; }
  .contact__role { color: var(--ink); font-size: 12.5px; margin-top: 4px; }
  .contact__list { list-style: none; margin-top: 18px; }
  .contact__line {
    display: flex; align-items: center; gap: 6px;
    color: var(--ink); font-size: 12.5px; line-height: 17px;
  }
  .contact__icon { width: 10px; height: 10px; flex: none; fill: var(--green); }
</style>
</head>
<body>
  <section class="card card--front" aria-label="Card front">
    <div class="brand"><span class="brand__square"></span>Pixel Harbor</div>
    <ul class="services">
      <li class="services__item">Ad Operations</li>
      <li class="services__item">Web Development</li>
      <li class="services__item">Hosting</li>
      <li class="services__item">Site Speed</li>
      <li class="services__item">Social Media</li>
      <li class="services__item">SEO</li>
    </ul>
  </section>

  <section class="card card--back" aria-label="Card back">
    <div class="brand"><span class="brand__square"></span>Pixel Harbor</div>
    <div class="contact">
      <h1 class="contact__name">Dana Welloby</h1>
      <p class="contact__role">President</p>
      <ul class="contact__list">
        <li class="contact__line">
          <svg class="contact__icon" viewBox="0 0 10 10"><circle cx="5" cy="5" r="5"/><path d="M3.3 2.6l1 1-.5.6a4 4 0 0 0 2 2l.6-.5 1 1-.7.8C4.8 7.4 2.6 5.2 2.5 3.3z" fill="#fff"/></svg>
          555.318.4406
        </li>
        <li class="contact__line">
          <svg class="contact__icon" viewBox="0 0 10 10"><rect x="0" y="2" width="10" height="6.5"/><path d="M0 2l5 3.5L10 2" stroke="#fff" stroke-width="0.9" fill="none"/></svg>
          dana@pixelharbor.example
        </li>
        <li class="contact__line">
          <svg class="contact__icon" viewBox="0 0 10 10"><circle cx="5" cy="5" r="5"/><path d="M0 5h10M5 0v10M5 0c-2.6 2.6-2.6 7.4 0 10M5 0c2.6 2.6 2.6 7.4 0 10" stroke="#fff" stroke-width="0.7" fill="none"/></svg>
          www.pixelharbor.example
        </li>
      </ul>
    </div>
  </section>
</body>
</html>
```